Web Site design for Computer Security Company

Would like a "web 2.0", parralax style website created for a internet security company called "BrightFerns". Really like the way a website like pelomintra.com looks. Like to have 3 steps like they do to explain our product/service.

1# Identify #2Analyze #3Educate

Would like the website to expand with additional information if they click on any of the items 1-3.

Have attached a logo to get an idea of colors. Would like a clean white background.

Pages: (could be one long page or individual pages, I'm open to ideas)

Home
About Us
Services
Contact us

Theme ideas: Research, Security, Lab, Education

Do not want a dark site with typical hacker images etc. Would like to portray the image that we are experts, and we will work with our customers to identify their risk areas on the internet, then train their users around security awareness.

Target Market(s)

Financial

Industry/Entity Type

Computer Security

Coding

Coded - Design and coding required

Number of Pages Required

4 page

Font styles to use
Sans Serif

Colors
33a6d7
0555a3
9bcb3b
ffffff

Requirements
Must have
• Clean web2.0 look.
• White background
• Threat, security, education, R&D are themes.
• working with logo to integrate a common color scheme.
• design feel like pelomintra.com
Nice to have
• Parralax or similar style page that expands for certain areas.
Should not have
• must not be black/dark with hacker images

```html
<!DOCTYPE html>
<html lang="en">
<head>
<meta charset="utf-8">
<title>BrightFerns – Secure Your People</title>
<link rel="stylesheet" href="https://fonts.googleapis.com/css2?family=Roboto:wght@300;400;500;700&display=swap">
<style>
:root{
  --blue:#2e9ed9;
  --blue-dark:#1f86c2;
  --navy:#0b3a66;
  --navy-deep:#082f55;
  --ink:#2d4657;
  --text:#5e6a72;
  --muted:#9aa3a9;
  --line:#cfd6db;
  --grey-band:#efefef;
  --white:#ffffff;
}
*{box-sizing:border-box;margin:0;padding:0}
html,body{width:1200px;height:2651px;overflow:hidden}
body{position:relative;background:var(--white);font-family:"Roboto",Arial,sans-serif;color:var(--text)}

/* header */
.site-header{position:absolute;left:0;top:0;width:1200px;height:125px;border-top:4px solid var(--blue);background:var(--white)}
.brand{position:absolute;left:78px;top:30px;width:140px;text-align:center}
.brand-mark{display:block;width:40px;height:40px;margin:0 auto 4px;border-radius:50%;background:var(--blue)}
.brand-name{font-size:22px;font-weight:700;color:var(--navy);line-height:1}
.brand-tag{font-size:8px;font-weight:500;color:var(--navy);letter-spacing:.5px;margin-top:3px}
.header-phone{position:absolute;left:934px;top:20px;font-size:25px;color:var(--blue);display:flex;align-items:center;gap:10px}
.main-nav{position:absolute;top:62px;left:514px;display:flex;align-items:center;height:49px}
.nav-item{font-size:17px;color:#222;text-transform:uppercase;margin-right:48px}
.nav-item.active{background:var(--blue);color:var(--white);padding:0 31px;height:49px;line-height:49px;border-radius:2px}
.nav-search{position:absolute;left:1100px;top:74px}

/* hero */
.hero{position:absolute;left:0;top:125px;width:1200px;height:552px;
  background:radial-gradient(ellipse at 50% 110%,#6fb6ef 0%,#1d5ea8 30%,#0e2f66 60%,#0a1d45 100%)}
.hero-title{position:absolute;left:0;top:168px;width:1200px;text-align:center;font-size:63px;font-weight:500;color:var(--white);letter-spacing:1px}
.hero-lead{position:absolute;left:140px;top:250px;width:920px;text-align:center;font-size:17px;line-height:28px;color:var(--white)}
.hero-cta{position:absolute;left:486px;top:324px;width:228px;height:60px;line-height:60px;text-align:center;background:var(--blue);color:var(--white);font-size:20px;border-radius:3px}
.hero-arrow{position:absolute;top:236px}

/* steps */
.steps{position:absolute;left:78px;top:595px;width:1044px;height:426px;box-shadow:0 6px 6px -4px rgba(0,0,0,.08)}
.step{position:absolute;top:0;width:332px}
.step-photo{width:332px;height:213px;border:7px solid var(--white);box-shadow:0 0 0 1px #e5e5e5}
.step-title{margin:20px 0 0 12px;font-size:19px;color:var(--ink);font-weight:500}
.step-text{margin:8px 0 0 12px;width:318px;font-size:14.5px;line-height:26px;color:var(--text)}
.step-more{margin:8px 0 0 12px;font-size:14.5px;font-weight:500;color:var(--blue-dark)}

/* welcome */
.welcome-mark{position:absolute;left:575px;top:1056px;width:50px;height:50px;border-radius:50%;background:var(--blue)}
.section-title{font-size:41px;font-weight:400;color:var(--ink)}
.welcome-title{position:absolute;left:0;top:1140px;width:1200px;text-align:center}
.welcome-text{position:absolute;left:140px;top:1230px;width:920px;text-align:center;font-size:14.5px;line-height:27px;color:var(--text)}
.btn{position:absolute;background:var(--blue);color:var(--white);font-size:21px;text-align:center;border-radius:3px}

/* about */
.about{position:absolute;left:0;top:1470px;width:1200px;height:416px;background:var(--grey-band)}
.about-title{position:absolute;left:80px;top:30px}
.about-text{position:absolute;left:80px;top:118px;width:635px;font-size:14.5px;line-height:28px;color:#454f56}
.about-text p+p{margin-top:2px}
.about-person{position:absolute;left:725px;top:0;width:397px;height:416px;background:linear-gradient(160deg,#e9e9e9 0%,#c9ccce 45%,#3b4a52 75%,#1f2a30 100%)}

/* contact */
.contact-title{position:absolute;left:0;top:1925px;width:1200px;text-align:center}
.contact-sub{position:absolute;left:0;top:1990px;width:1200px;text-align:center;font-size:19px;color:#555}
.field{position:absolute;border:1px solid var(--line);border-radius:3px;background:var(--white);font-size:13px;color:var(--muted);padding:16px 0 0 13px}
.field.focus{border-color:var(--blue)}

/* footer */
.site-footer{position:absolute;left:0;top:2329px;width:1200px;height:263px;background:linear-gradient(180deg,var(--navy) 0%,var(--navy-deep) 100%);border-top:3px solid var(--blue)}
.foot-head{position:absolute;top:38px;font-size:18px;font-weight:500;color:var(--blue)}
.foot-links{position:absolute;left:80px;top:80px;list-style:none;font-size:14.5px;line-height:31px;color:#dfe8ef}
.foot-links li:first-child{color:var(--blue)}
.foot-contact{position:absolute;left:345px;top:68px;width:230px;font-size:14.5px;color:#dfe8ef}
.foot-row{display:flex;gap:14px;margin-bottom:14px;line-height:22px}
.foot-row svg{flex:none;margin-top:3px}
.foot-map{position:absolute;left:610px;top:71px;width:251px;height:141px;background:linear-gradient(135deg,#eef0ec 0%,#dfe4dc 100%);border:2px solid #d9dde0}
.foot-brand{position:absolute;left:900px;top:28px;width:196px;text-align:center;color:var(--white)}
.foot-brand .brand-mark{width:44px;height:44px;background:var(--white)}
.foot-brand .brand-name{color:var(--white);font-size:26px}
.foot-brand .brand-tag{color:var(--white);font-size:9px}
.socials{position:absolute;left:925px;top:169px;display:flex;gap:13px}
.social{width:40px;height:40px;border-radius:50%;background:var(--blue)}
.copy-bar{position:absolute;left:0;top:2592px;width:1200px;height:59px;background:var(--blue);text-align:center;line-height:59px;font-size:14.5px;color:#0d3357}
.copy-bar b{color:var(--white);font-weight:700}
</style>
</head>
<body>

<header class="site-header">
  <div class="brand">
    <span class="brand-mark"></span>
    <div class="brand-name">BrightFerns</div>
    <div class="brand-tag">SECURE YOUR PEOPLE</div>
  </div>
  <div class="header-phone">
    <svg width="26" height="26" viewBox="0 0 24 24"><path fill="#2e9ed9" d="M6.6 10.8a15.2 15.2 0 0 0 6.6 6.6l2.2-2.2c.3-.3.7-.4 1-.2 1.1.4 2.3.6 3.6.6.6 0 1 .4 1 1V20c0 .6-.4 1-1 1A17 17 0 0 1 3 4c0-.6.4-1 1-1h3.5c.6 0 1 .4 1 1 0 1.3.2 2.5.6 3.6.1.3 0 .7-.2 1z"/></svg>
    123 456 7890
  </div>
  <nav class="main-nav">
    <span class="nav-item active">Home</span>
    <span class="nav-item">About Us</span>
    <span class="nav-item">Services</span>
    <span class="nav-item">Contact Us</span>
  </nav>
  <svg class="nav-search" width="22" height="22" viewBox="0 0 22 22"><circle cx="9" cy="9" r="7" fill="none" stroke="#111" stroke-width="3"/><line x1="14" y1="14" x2="20" y2="20" stroke="#111" stroke-width="3.5" stroke-linecap="round"/></svg>
</header>

<section class="hero" role="img" aria-label="Glowing network of padlock icons over the curve of the earth">
  <svg class="hero-arrow" style="left:14px" width="50" height="50" viewBox="0 0 50 50"><circle cx="25" cy="25" r="23" fill="none" stroke="#3a7fc4" stroke-width="2"/><path d="M29 15 19 25l10 10" fill="none" stroke="#3a7fc4" stroke-width="2.5"/></svg>
  <svg class="hero-arrow" style="left:1136px" width="50" height="50" viewBox="0 0 50 50"><circle cx="25" cy="25" r="23" fill="none" stroke="#3a7fc4" stroke-width="2"/><path d="M21 15l10 10-10 10" fill="none" stroke="#3a7fc4" stroke-width="2.5"/></svg>
  <h1 class="hero-title">SECURE YOUR PEOPLE</h1>
  <p class="hero-lead">BrightFerns is a leader in Social Engineering and Security awareness education. Our cutting-edge analytics software is a first of its kind to truly identify an organizations attack surface to provide</p>
  <div class="hero-cta">CONTACT US NOW</div>
</section>

<section class="steps">
  <article class="step" style="left:0">
    <div class="step-photo" role="img" aria-label="Digital fingerprint and identity scan interface" style="background:linear-gradient(135deg,#1a3fa8,#2e6fe0 55%,#0f2a7a)"></div>
    <h3 class="step-title">IDENTIFY</h3>
    <p class="step-text">BrightFerns has developed industry leading software that will intelligently build a profile of a company's attack surface.</p>
    <div class="step-more">READ MORE... &#187;</div>
  </article>
  <article class="step" style="left:356px">
    <div class="step-photo" role="img" aria-label="Analyst working at screens in a monitoring room" style="background:linear-gradient(135deg,#cfd8e2,#6d8fb3 50%,#2b3a52)"></div>
    <h3 class="step-title">ANALYZE</h3>
    <p class="step-text">One the attack surface has been realized, the BrightFerns analytics engine(s) is used to further identify relationships between..</p>
    <div class="step-more">READ MORE... &#187;</div>
  </article>
  <article class="step" style="left:712px">
    <div class="step-photo" role="img" aria-label="Team of security trainers standing together in an office" style="background:linear-gradient(135deg,#3b4b5a,#7a6f72 50%,#2a3440)"></div>
    <h3 class="step-title">EDUCATE</h3>
    <p class="step-text">After the attack surface has been mapped out, and security assessments have been perform-ed, BrightFerns provides an in-depth..</p>
    <div class="step-more">READ MORE... &#187;</div>
  </article>
</section>

<span class="welcome-mark"></span>
<h2 class="section-title welcome-title">WELCOME TO BRIGHTFERNS</h2>
<p class="welcome-text">BrightFerns is a leader in Social Engineering and Security awareness education. Our cutting-edge analytics software is a first of its kind to truly identify an organizations attack surface to provide realistic assessments that identify users overall security awareness level. This is follow-up with custom tailored training material that not only has been designed for individual markets, but also specific regulations. This ensures that all users have been trained to help limit risk and exposure for an organization.</p>
<div class="btn" style="left:516px;top:1352px;width:166px;height:56px;line-height:56px">KNOW MORE</div>

<section class="about">
  <h2 class="section-title about-title">ABOUT US</h2>
  <div class="about-text">
    <p>BrightFerns is a leader in Social Engineering and Security awareness education. Our cutting-edge analytics software is a first of its kind to truly identify an organizations attack surface to provide realistic assessments that identify users overall security awareness level.</p>
    <p>This is follow-up with custom tailored training material that not only has been designed for individual markets, but also specific regulations. This ensures that all users have been trained to help limit risk and exposure for an organization.</p>
  </div>
  <div class="btn" style="left:78px;top:295px;width:166px;height:55px;line-height:55px">KNOW MORE</div>
  <div class="about-person" role="img" aria-label="Smiling professional holding a laptop and pointing forward"></div>
</section>

<h2 class="section-title contact-title">CONTCT US</h2>
<p class="contact-sub">Need a free quote, or have a question? Get in touch!</p>
<div class="field focus" style="left:231px;top:2034px;width:366px;height:51px">Name *</div>
<div class="field" style="left:604px;top:2034px;width:364px;height:51px">Email *</div>
<div class="field" style="left:231px;top:2092px;width:366px;height:51px">Phone *</div>
<div class="field" style="left:604px;top:2092px;width:364px;height:110px">Message *</div>
<div class="field" style="left:231px;top:2150px;width:366px;height:52px">Subject *</div>
<div class="btn" style="left:521px;top:2209px;width:157px;height:56px;line-height:56px;font-size:20px">SUBMIT</div>

<footer class="site-footer">
  <h4 class="foot-head" style="left:80px">Sitemap</h4>
  <ul class="foot-links">
    <li>Home</li><li>About Us</li><li>Services</li><li>Contact Us</li>
  </ul>
  <h4 class="foot-head" style="left:345px">Keep in Touch</h4>
  <div class="foot-contact">
    <div class="foot-row">
      <svg width="18" height="22" viewBox="0 0 18 22"><path d="M9 0v22M2 4h14l-2 3 2 3H2zM16 12H4l-2 3 2 3h12z" fill="#2e9ed9" stroke="#2e9ed9" stroke-width="2"/></svg>
      <span>101 - Lorem ipsum is simple dummy text of print and type setting industry.</span>
    </div>
    <div class="foot-row">
      <svg width="18" height="18" viewBox="0 0 24 24"><path fill="#2e9ed9" d="M6.6 10.8a15.2 15.2 0 0 0 6.6 6.6l2.2-2.2c.3-.3.7-.4 1-.2 1.1.4 2.3.6 3.6.6.6 0 1 .4 1 1V20c0 .6-.4 1-1 1A17 17 0 0 1 3 4c0-.6.4-1 1-1h3.5c.6 0 1 .4 1 1 0 1.3.2 2.5.6 3.6.1.3 0 .7-.2 1z"/></svg>
      <span>123 456 7890</span>
    </div>
    <div class="foot-row">
      <svg width="18" height="14" viewBox="0 0 18 14"><rect width="18" height="14" rx="1" fill="#2e9ed9"/><path d="M1 1l8 6 8-6" fill="none" stroke="#0b3a66" stroke-width="1.5"/></svg>
      <span>info@BrightFerns.com</span>
    </div>
  </div>
  <h4 class="foot-head" style="left:608px">Map</h4>
  <div class="foot-map" role="img" aria-label="Street map showing the office location"></div>
  <div class="foot-brand">
    <span class="brand-mark"></span>
    <div class="brand-name">BrightFerns</div>
    <div class="brand-tag">SECURE YOUR PEOPLE</div>
  </div>
  <div class="socials">
    <span class="social"></span><span class="social"></span><span class="social"></span>
  </div>
</footer>
<div class="copy-bar">&copy;<b>BRIGHTFERNS</b> - 2016. All Rights Reserved</div>

</body>
</html>
```